Stickers to put on my honeyglasses

Stickers for my honey glasses.
Only a single sticker on the front. Same should have a stripe on the top side which goes above the lid to show if the glass was opened.
Size of the main part should be 55mm high and max. 100 mm wide.
The stripe on the top should be 70mm long.
I added a Picture of another producer which uses the same glass as I do.
I should say: 'e Lendorf Glas Hunneg'. which means 'another glass of honey. 'Hunneg' should be mainly visible and therefore very large. 'e Lendorf Glas' should be less visible and therefore smaller above the 'Hunneg'
- It needs to contain the quantity : '500gr'
- It needs to contain my Name and address: 'Marc Lendorf, 38, rue Ferd Lusang, L-9241 Miersch' (This should be small and not to visible)
- It needs to conatin a validity Line: ´Am beschte virum:` (With enough space so I can add a date by hand)
- It needs to say: 'dréchen, kill andäischterstockéieren' (to store it dry cold and dark)

```html
<!DOCTYPE html>
<html lang="lb">
<head>
<meta charset="utf-8">
<title>Hunneg Etikett</title>
<link rel="stylesheet" href="https://fonts.googleapis.com/css2?family=Marcellus&family=Questrial&family=Poppins:ital,wght@0,600;1,400&display=swap">
<style>
  :root {
    --page-bg: #c0c0c0;
    --honey-light: #fdc832;
    --honey-deep: #f6ae18;
    --honey-red: #c8372d;
    --ink-brown: #4a2a10;
    --muted-brown: #8a5a1c;
    --white: #ffffff;
    --comb-orange: #f29a12;
    --comb-light: #ffd35a;
  }
  html, body {
    margin: 0;
    width: 1200px;
    height: 1200px;
    overflow: hidden;
    background: var(--page-bg);
  }
  .sticker {
    position: absolute;
    left: 139px;
    top: 115px;
    width: 922px;
    height: 969px;
  }
  .sticker-shape {
    position: absolute;
    inset: 0;
  }
  .label-content {
    position: absolute;
    left: 0;
    top: 456px;
    width: 922px;
    height: 513px;
  }
  .tagline {
    position: absolute;
    top: 46px;
    width: 100%;
    text-align: center;
    font-family: "Questrial", sans-serif;
    font-size: 36px;
    color: var(--ink-brown);
    font-weight: 600;
  }
  .product-name {
    position: absolute;
    top: 78px;
    width: 100%;
    text-align: center;
    font-family: "Marcellus", serif;
    font-size: 150px;
    line-height: 1;
    letter-spacing: 2px;
    color: var(--honey-red);
  }
  .quantity {
    position: absolute;
    left: 380px;
    top: 251px;
    width: 162px;
    height: 50px;
    background: var(--honey-red);
    clip-path: polygon(12% 0, 88% 0, 100% 50%, 88% 100%, 12% 100%, 0 50%);
    color: var(--white);
    font-family: "Poppins", sans-serif;
    font-weight: 600;
    font-size: 31px;
    line-height: 50px;
    text-align: center;
  }
  .best-before {
    position: absolute;
    left: 146px;
    top: 328px;
    font-family: "Questrial", sans-serif;
    font-size: 33px;
    color: var(--ink-brown);
    line-height: 57px;
  }
  .date-field {
    position: absolute;
    left: 465px;
    top: 328px;
    width: 306px;
    height: 57px;
    background: var(--white);
    border-radius: 29px;
  }
  .storage-note {
    position: absolute;
    top: 400px;
    left: 90px;
    width: 100%;
    text-align: center;
    font-family: "Poppins", sans-serif;
    font-style: italic;
    font-size: 28px;
    color: var(--ink-brown);
  }
  .producer-address {
    position: absolute;
    top: 460px;
    left: 90px;
    width: 100%;
    text-align: center;
    font-family: "Questrial", sans-serif;
    font-size: 17px;
    color: var(--muted-brown);
  }
  .bee-illustration {
    position: absolute;
    left: 14px;
    top: 196px;
    width: 170px;
    height: 262px;
    background: radial-gradient(circle at 55% 45%, var(--comb-light), var(--comb-orange) 75%);
    clip-path: polygon(40% 0, 80% 8%, 100% 40%, 88% 78%, 50% 100%, 10% 88%, 0 50%, 12% 18%);
  }
</style>
</head>
<body>
  <div class="sticker">
    <svg class="sticker-shape" width="922" height="969" viewBox="0 0 922 969" aria-hidden="true">
      <defs>
        <linearGradient id="honeyFill" x1="0" y1="0" x2="1" y2="1">
          <stop offset="0" stop-color="var(--honey-light)"/>
          <stop offset="1" stop-color="var(--honey-deep)"/>
        </linearGradient>
      </defs>
      <rect class="seal-strip" x="373.5" y="0" width="175" height="480" rx="8" fill="url(#honeyFill)"/>
      <polygon class="label-body"
               points="98,468 824,468 908,712 824,957 98,957 14,712"
               fill="url(#honeyFill)" stroke="url(#honeyFill)" stroke-width="24" stroke-linejoin="round"/>
    </svg>

    <div class="label-content">
      <div class="bee-illustration" role="img" aria-label="Illustration of a honey bee sitting on golden honeycomb cells"></div>
      <div class="tagline">e Lendorf Glas Hunneg</div>
      <div class="product-name">HUNNEG</div>
      <div class="quantity">500gr</div>
      <div class="best-before">Am beschte virum:</div>
      <div class="date-field"></div>
      <div class="storage-note">dréchen, kill andäischterstockéieren</div>
      <div class="producer-address">Marc Lendorf, 38, rue Ferd Lusang, L-9241 Miersch</div>
    </div>
  </div>
</body>
</html>
```